Business Cards for IT Consulting Company (Managed Service Provider)

I am looking to have some business cards printed and would like some designs. We are an IT Consulting company based in Vancouver BC. I would like a nice clean and modern look to the cards. I have uploaded all the versions of my logo so parts can be used as needed. Here is a snippit from our website homepage:

Kelbrook Systems Ltd. is an IT Solutions Partner located in Vancouver BC, Canada. We offer IT solutions and support to customers in the greater Vancouver Area. With expertise in Microsoft platforms, as well as Linux and Mac OSX and over 12 years experience in the IT industry, Kelbrook Systems is dedicated to offering our clients top quality service and products. We take pride in the solutions we offer our customers. The greatest compliment a client can give us is to recommend our services.

Kelbrook Systems Ltd. offers a wide range of IT services from onsite service to remote support and managed service solutions. This allows clients to choose the support path that best suits their company’s needs. Supporting many different sized companies from small to enterprise level over the past 12 years Kelbrook Systems has the experience and expertise needed to ensure things run smoothly. Allowing our clients to focus on doing business.

Revolutionizing the way IT services are delivered.

Kelbrook Systems is dedicated to providing our clients with IT solutions that work and grow with them for years to come. This philosophy helps save money in the long run instead of replacing equipment constantly. Far too often IT solutions are not well thought out and while possibly solving the problem at hand, require replacement due to growth or quality within a very short time frame. Kelbrook Systems takes pride in providing solutions that will last and be able to accommodate growth without the need for replacement.

Industry/Entity Type

Information Technology

Contact Information for Business Card

Kelbrook Systems Ltd.
(Employee Name)
Eml: (Employees Email Address)
Web: kelbrook.me
Ph: 604-555-0142

Font styles to use
Serif
Sans Serif

Requirements
Must have
• The Company logo and company colors.
Nice to have
• - Our tag line: "Revolutionizing IT Services" or "Revolutionizing the way IT services are delivered."
• - Also I really like the idea of nature and technology together blending which is sort of where my logo came from so integrating that somehow onto the business cards would be great.

```html
<!DOCTYPE html>
<html lang="en">
<head>
<meta charset="utf-8">
<title>Kelbrook Systems Ltd. — Business Cards</title>
<link href="https://fonts.googleapis.com/css2?family=Questrial&family=Montserrat:wght@700&display=swap" rel="stylesheet">
<style>
  :root {
    --backdrop: #1b1b1d;
    --card-white: #ffffff;
    --brand-blue: #35a8e0;
    --brand-blue-light: #6cc2ec;
    --ink: #1e1e1e;
    --on-blue: #ffffff;
  }
  * { box-sizing: border-box; margin: 0; padding: 0; }
  html, body {
    width: 1200px; height: 937px; overflow: hidden;
    background: var(--backdrop);
    font-family: "Questrial", "Century Gothic", sans-serif;
  }
  .stage { position: relative; width: 1200px; height: 937px; }

  .card {
    position: absolute;
    width: 580px; height: 331px;
    border-radius: 22px;
    overflow: hidden;
    background: var(--card-white);
    box-shadow: 0 18px 40px rgba(0,0,0,.55);
  }
  .card--back  { left: 560px; top: 90px; }
  .card--front { left: 60px;  top: 500px; }

  .brand {
    display: flex; align-items: center; gap: 12px;
    color: var(--brand-blue);
    font-family: "Questrial", sans-serif;
    font-weight: 400;
    white-space: nowrap;
  }
  .brand__mark {
    width: 30px; height: 30px;
    background: var(--brand-blue);
    flex: none;
  }
  .brand__name { font-size: 40px; letter-spacing: .5px; line-height: 1; }

  /* back */
  .card--back .brand { position: absolute; left: 0; right: 0; top: 118px; justify-content: center; }
  .tagline {
    position: absolute; left: 0; right: 0; top: 228px;
    text-align: center;
    font-size: 17px; color: var(--ink); letter-spacing: .3px;
  }

  /* front */
  .front-bands { position: absolute; inset: 0; width: 100%; height: 100%; }
  .card--front .brand { position: absolute; left: 34px; top: 122px; gap: 10px; }
  .card--front .brand__mark { width: 26px; height: 26px; }
  .card--front .brand__name { font-size: 32px; }

  .contact {
    position: absolute; right: 30px; bottom: 26px;
    text-align: right;
    color: var(--on-blue);
    line-height: 1.32;
  }
  .contact__name { font-family: "Montserrat", sans-serif; font-weight: 700; font-size: 17px; letter-spacing: .6px; }
  .contact__role { font-size: 15px; margin-bottom: 4px; }
  .contact__line { display: flex; align-items: center; justify-content: flex-end; gap: 8px; font-size: 15px; }
  .contact__icon { width: 14px; height: 14px; flex: none; }
</style>
</head>
<body>
<main class="stage">

  <section class="card card--back" aria-label="Card back">
    <div class="brand">
      <span class="brand__mark"></span>
      <span class="brand__name">Kelbrook Systems</span>
    </div>
    <p class="tagline">Revolutionizing the way IT services are delivered</p>
  </section>

  <section class="card card--front" aria-label="Card front">
    <svg class="front-bands" viewBox="0 0 580 331" preserveAspectRatio="none" aria-hidden="true">
      <defs>
        <linearGradient id="band-sheen" x1="0" y1="1" x2="1" y2="0">
          <stop offset="0" stop-color="var(--brand-blue)"/>
          <stop offset=".35" stop-color="var(--brand-blue-light)"/>
          <stop offset=".6" stop-color="var(--brand-blue)"/>
        </linearGradient>
      </defs>
      <polygon points="0,0 230,0 0,105" fill="var(--brand-blue)"/>
      <polygon points="545,0 580,0 580,331 235,331" fill="url(#band-sheen)"/>
    </svg>

    <div class="brand">
      <span class="brand__mark"></span>
      <span class="brand__name">Kelbrook Systems</span>
    </div>

    <div class="contact">
      <p class="contact__name">Daniel Marsh</p>
      <p class="contact__role">Network Engineer</p>
      <p class="contact__line">604-555-0142
        <svg class="contact__icon" viewBox="0 0 24 24"><path fill="currentColor" d="M6.6 10.8a15.1 15.1 0 0 0 6.6 6.6l2.2-2.2a1 1 0 0 1 1-.25 11.4 11.4 0 0 0 3.6.57 1 1 0 0 1 1 1V20a1 1 0 0 1-1 1A17 17 0 0 1 3 4a1 1 0 0 1 1-1h3.5a1 1 0 0 1 1 1c0 1.25.2 2.45.57 3.570a1 1 0 0 1-.25 1z"/></svg>
      </p>
      <p class="contact__line">dmarsh@kelbrook.me
        <svg class="contact__icon" viewBox="0 0 24 24"><rect x="2" y="5" width="20" height="14" rx="1.5" fill="none" stroke="currentColor" stroke-width="2"/><path d="M3 6l9 7 9-7" fill="none" stroke="currentColor" stroke-width="2"/></svg>
      </p>
      <p class="contact__line">www.kelbrook.me
        <svg class="contact__icon" viewBox="0 0 24 24" fill="none" stroke="currentColor" stroke-width="1.8"><circle cx="12" cy="12" r="10"/><ellipse cx="12" cy="12" rx="4.5" ry="10"/><path d="M2 12h20M4 7h16M4 17h16"/></svg>
      </p>
    </div>
  </section>

</main>
</body>
</html>
```